Nordic Joinery Guild Wordpress Theme and newsletter template

We at the NJG are looking to start a Wordpress website and also send out a newsletter (web). We have just completed a Logo design project with ArtFlockly and we were so pleased with the results that we would like to see what the designers can come up with for a Wordpress theme and a template for an online newsletter. The theme has to support Icelandic letters. It also has to have a subscription option by email. We would need to have the option to add advertisement banners. The theme has to be easy to work with.
Below we have added a two websites for a example of what we are looking for: .
http://www.torvexhub.example/
http://www.brakkel.example/
The newsletter has to have a similar theme as the website and will be used with MS Publisher.

Attached is the new NJG logo.
Updates

Project Deadline Extended Reason: Not fully happy with the designs we have gotten so far. Would like to extend time to see if improvements can be made. Added Tuesday, June 16, 2015

Target Market(s)

Welding association members, welding and metalworking industry, suppliers in welding industry, International welding community, other national welding associations, welding education community

Industry/Entity Type

Welding

Number of Pages Required

3 page

Requirements
Must have
• The TKBÓ logo
• Icelandic letters
• email formpage
• Advertisement space/banners/buttons
• Easy to manage
• Compatible with Wordpress
Nice to have
• Welding pictures
• Nice graphics
Should not have
• Should not be dark and heavy set.

```html
<!DOCTYPE html>
<html lang="is">
<head>
<meta charset="utf-8">
<title>TKBÓ – Nordic Joinery Guild</title>
<link rel="stylesheet" href="https://fonts.googleapis.com/css2?family=Open+Sans:wght@300;400;600;700&family=Arimo:wght@400;700&display=swap">
<style>
:root{
  --blue:#0089c3;
  --blue-dark:#0a6f9e;
  --white:#ffffff;
  --text:#6d6d6d;
  --ink:#1b1b1b;
  --grey-band:#bdbdbd;
  --footer:#333333;
  --field:#ffffff;
  --accent-red:#d42a2a;
}
*{box-sizing:border-box;margin:0;padding:0}
html,body{width:1200px;height:3529px;overflow:hidden;background:var(--white)}
body{font-family:"Open Sans",Arial,sans-serif;color:var(--text);position:relative}

.site-header{position:absolute;left:0;top:0;width:1200px;height:188px;background:var(--white)}
.brand{position:absolute;left:44px;top:40px;display:flex;align-items:center;gap:16px}
.brand-dot{width:28px;height:28px;border-radius:50%;background:var(--blue)}
.brand-name{font-family:"Open Sans",Arial,sans-serif;font-weight:700;font-size:64px;color:var(--blue);letter-spacing:1px;line-height:1}
.lang-flags{position:absolute;left:1082px;top:38px;display:flex;gap:14px}
.account-links{position:absolute;right:47px;top:84px;font-size:16px;color:var(--ink)}
.search-box{position:absolute;left:976px;top:113px;width:177px;height:33px;border:1px solid #cfcfcf;background:var(--white)}
.search-box svg{position:absolute;right:8px;top:7px}

.main-nav{position:absolute;left:0;top:188px;width:1200px;height:66px;background:var(--blue);display:flex;justify-content:center;align-items:center}
.main-nav a,.footer-nav a{color:var(--white);text-decoration:none;font-family:"Arimo",Arial,sans-serif;font-size:11.5px;text-transform:uppercase;margin:0 19px}

.hero{position:absolute;left:0;top:254px;width:1200px;height:452px;overflow:hidden}
.hero-photo{position:absolute;inset:0;background:linear-gradient(100deg,#2b3a4a 0%,#5b6c7d 30%,#8a98a4 50%,#2c4f8f 65%,#6c5a45 85%,#3a3430 100%)}
.hero-mask{position:absolute;inset:0}
.hero-title{position:absolute;left:138px;top:46px;font-family:"Arimo",Arial,sans-serif;color:var(--ink);line-height:1}
.hero-title .line-1{font-size:54px;font-weight:700;display:block}
.hero-title .line-2{font-size:54px;font-weight:400;display:block;margin-top:4px}
.hero-month{position:absolute;left:532px;top:20px;font-family:"Arimo",Arial,sans-serif;font-weight:700;font-size:48px;color:var(--white)}
.hero-arrow{position:absolute}
.hero-strip{position:absolute;left:0;top:706px;width:1200px;height:71px;background:var(--blue)}
.hero-dots{position:absolute;left:556px;top:735px;display:flex;gap:17px}
.hero-dots span{width:11px;height:11px;border-radius:50%;background:#5fc2ea}
.hero-dots span.active{background:#1a4c66}

.about{position:absolute;left:47px;top:872px;width:1106px;text-align:center}
.section-title{font-size:30px;font-weight:400;color:var(--blue);letter-spacing:1px}
.about p{margin-top:32px;font-size:17.5px;line-height:25px;color:var(--text)}

.whats-new{position:absolute;left:0;top:1188px;width:1200px;height:605px;background:var(--blue)}
.whats-new-notch{position:absolute;left:574px;top:1792px}
.whats-new h2{position:absolute;left:0;top:50px;width:1200px;text-align:center;font-weight:300;font-size:60px;color:var(--white);letter-spacing:1px}
.news-card{position:absolute;top:158px;width:254px;height:339px;background:var(--white);box-shadow:0 2px 6px rgba(0,0,0,.25)}
.news-image{width:254px;height:273px}
.news-card p{font-size:13px;line-height:21px;text-align:center;color:var(--text);padding-top:12px}

.join{position:absolute;left:343px;top:1887px;width:551px;height:541px;background:var(--blue);box-shadow:0 2px 6px rgba(0,0,0,.25)}
.join h2{position:absolute;left:0;top:42px;width:551px;text-align:center;font-weight:400;font-size:30px;color:var(--white)}
.join-field{position:absolute;left:99px;width:353px;height:47px;background:var(--field);font-size:13px;color:#8a8a8a;padding:13px 10px;text-transform:uppercase}
.join-send{position:absolute;left:219px;top:452px;width:116px;height:40px;background:var(--white);color:#555;font-size:16px;text-align:center;line-height:40px;letter-spacing:1px;box-shadow:0 2px 4px rgba(0,0,0,.25)}

.partners{position:absolute;left:0;top:2586px;width:1200px;height:501px;background:var(--grey-band)}
.partner-card{position:absolute;top:75px;width:254px;height:339px;background:var(--white);display:flex;align-items:center;justify-content:center;text-align:center;box-shadow:0 2px 6px rgba(0,0,0,.2)}
.partner-card span{font-weight:700;font-size:26px;color:#2a3d6b;line-height:1.2;padding:0 16px}

.thanks{position:absolute;left:0;top:3154px;width:1200px;text-align:center;font-family:"Arimo",Arial,sans-serif;font-size:36px;color:var(--ink)}

.site-footer{position:absolute;left:0;top:3264px;width:1200px;height:265px;background:var(--footer)}
.footer-nav{position:absolute;left:0;top:88px;width:1200px;display:flex;justify-content:center}
.copyright{position:absolute;left:0;top:228px;width:1200px;text-align:center;font-size:11px;color:#cfcfcf}
</style>
</head>
<body>

<header class="site-header">
  <div class="brand"><span class="brand-dot"></span><span class="brand-name">TKBÓ</span></div>
  <div class="lang-flags">
    <svg width="30" height="20" viewBox="0 0 30 20" aria-label="English">
      <rect width="30" height="20" fill="#1f3a8a"/>
      <path d="M0 0L30 20M30 0L0 20" stroke="#fff" stroke-width="4"/>
      <path d="M0 0L30 20M30 0L0 20" stroke="#c8102e" stroke-width="1.5"/>
      <rect x="12" width="6" height="20" fill="#fff"/><rect y="7" width="30" height="6" fill="#fff"/>
      <rect x="13.5" width="3" height="20" fill="#c8102e"/><rect y="8.5" width="30" height="3" fill="#c8102e"/>
    </svg>
    <svg width="30" height="20" viewBox="0 0 30 20" aria-label="Íslenska">
      <rect width="30" height="20" fill="#1e3f9a"/>
      <rect x="8" width="6" height="20" fill="#fff"/><rect y="7" width="30" height="6" fill="#fff"/>
      <rect x="9.5" width="3" height="20" fill="#d72828"/><rect y="8.5" width="30" height="3" fill="#d72828"/>
    </svg>
  </div>
  <div class="account-links">Login &nbsp;/&nbsp; Register</div>
  <div class="search-box">
    <svg width="18" height="18" viewBox="0 0 18 18"><circle cx="7" cy="7" r="5" fill="none" stroke="#333" stroke-width="2"/><path d="M11 11l5 5" stroke="#333" stroke-width="2.5"/></svg>
  </div>
</header>

<nav class="main-nav">
  <a href="#">Home</a><a href="#">About</a><a href="#">Membership</a><a href="#">Events</a><a href="#">Publications</a><a href="#">Certifications</a><a href="#">Contact us</a>
</nav>

<section class="hero">
  <div class="hero-photo" role="img" aria-label="Welder in protective mask and gloves working on steel rebar at a construction site"></div>
  <svg class="hero-mask" width="1200" height="452" viewBox="0 0 1200 452">
    <path d="M0 0H240C120 30 40 60 0 90Z" fill="#fff"/>
    <path d="M0 300C80 380 180 430 330 452H0Z" fill="#fff"/>
    <path d="M1060 0H1200V240C1170 130 1120 50 1060 0Z" fill="#fff"/>
  </svg>
  <div class="hero-month">JUNE</div>
  <div class="hero-title"><span class="line-1">TKBÓ WELDING</span><span class="line-2">BUYERS GUIDE</span></div>
  <svg class="hero-arrow" style="left:1124px;top:36px" width="20" height="36" viewBox="0 0 20 36"><path d="M3 3l14 15L3 33" fill="none" stroke="#d8d8d8" stroke-width="3"/></svg>
  <svg class="hero-arrow" style="left:56px;top:378px" width="20" height="36" viewBox="0 0 20 36"><path d="M17 3L3 18l14 15" fill="none" stroke="#bdbdbd" stroke-width="3"/></svg>
</section>
<div class="hero-strip"></div>
<div class="hero-dots"><span class="active"></span><span></span><span></span><span></span></div>

<section class="about">
  <h2 class="section-title">ABOUT TKBÓ</h2>
  <p>"Sed ut perspiciatis unde omnis iste natus error sit voluptatem accusantium doloremque laudantium, totam rem aperiam, eaque ipsa quae ab illo inventore veritatis et quasi architecto beatae vitae dicta sunt explicabo. Nemo enim ipsam voluptatem quia voluptas sit aspernatur aut odit aut fugit, sed quia consequuntur magni dolores eos qui ratione voluptatem sequi nesciunt Neque porro quisquam est, qui dolorem ipsum quia dolor sit amet, consectetur, adipisci velit, sed quia non numquam eius modi tempora incidunt ut labore et dolore magnam aliquam quaerat voluptatem.</p>
</section>

<section class="whats-new">
  <h2>WHATS NEW</h2>
  <article class="news-card" style="left:52px"><div class="news-image" role="img" aria-label="Robotic welding arm throwing sparks in a factory" style="background:linear-gradient(135deg,#3a3a3a,#c9a23a 45%,#6e6a5a 70%,#2d2d2d)"></div><p>Sed ut perspiciatis unde ,<br>ipsa quae ab illo inventore.</p></article>
  <article class="news-card" style="left:332px"><div class="news-image" role="img" aria-label="Welder working on rebar at a building site" style="background:linear-gradient(160deg,#2d5fa8,#7f93a8 40%,#3a4f8c 65%,#5b4a38)"></div><p>Sed ut perspiciatis unde ,<br>ipsa quae ab illo inventore.</p></article>
  <article class="news-card" style="left:616px"><div class="news-image" role="img" aria-label="Welder in blue light with bright arc" style="background:linear-gradient(150deg,#0c3b6e,#2aa3c8 45%,#0f5d86 70%,#082a4a)"></div><p>Sed ut perspiciatis unde ,<br>ipsa quae ab illo inventore.</p></article>
  <article class="news-card" style="left:894px"><div class="news-image" role="img" aria-label="Industrial welding robot with orange arm and sparks" style="background:linear-gradient(140deg,#4a3a55,#d98a3a 40%,#c9c0d8 60%,#5a3a2a)"></div><p>Sed ut perspiciatis unde ,<br>ipsa quae ab illo inventore.</p></article>
</section>
<svg class="whats-new-notch" width="52" height="24" viewBox="0 0 52 24"><path d="M0 0H52L26 24Z" fill="#0089c3"/></svg>

<section class="join">
  <h2>JOIN US</h2>
  <div class="join-field" style="top:104px">Name:</div>
  <div class="join-field" style="top:170px">Email:</div>
  <div class="join-field" style="top:233px">Organisation:</div>
  <div class="join-field" style="top:299px;height:127px">Message:</div>
  <div class="join-send">SEND</div>
</section>

<section class="partners">
  <div class="partner-card" style="left:52px"><span>Corvane International</span></div>
  <div class="partner-card" style="left:335px"><span>Ridgeback Boilerworks</span></div>
  <div class="partner-card" style="left:612px"><span>Veltra</span></div>
  <div class="partner-card" style="left:894px"><span>KMF Kestrel Metal Forming</span></div>
</section>

<p class="thanks">Thank You for visiting our web site!</p>

<footer class="site-footer">
  <nav class="footer-nav">
    <a href="#">Home</a><a href="#">About</a><a href="#">Membership</a><a href="#">Events</a><a href="#">Publications</a><a href="#">Certifications</a><a href="#">Contact us</a>
  </nav>
  <p class="copyright">Copyright © 2015 Halvern Systems, Inc. All rights reserved.</p>
</footer>

</body>
</html>
```